Preferred pricing vendor

We are a plumbing company that has many services
-Boilers & Controls
-Plumbing & Heating
-HVAC & Refrigeration
-Preventative Maintenacne
-Gas fitting & Drain Cleaning

We primarily look after condo buildings, and our preferred service rates ($98, $93, or $88 depending on the contract) extend to all of our clients. So in essence, we look after the mechanical room and common equipment but our clients can call us in for drain cleaning or replacing a fixture in their suite. The discounted rates apply to the personal residence. We want a flyer to let them know they get a discount on our services. A one-pager we can send out to all of our contract clients.

Included source files for our letterhead and logo just so you can see the colours we go with.

Target Market(s)

Residential repairs, individual people, replacement of fixtures in-suite specific repairs

Requirements
Must have
• be colourful and attractive

```html
<!DOCTYPE html>
<html lang="en">
<head>
<meta charset="utf-8">
<title>Keystone Mechanical – Resident Discount Flyer</title>
<link rel="stylesheet" href="https://fonts.googleapis.com/css2?family=Montserrat:wght@400;500;600;700;800&display=swap">
<style>
  :root {
    --blue: #1f66b3;
    --blue-deep: #0f4f99;
    --orange: #e8562a;
    --white: #ffffff;
    --ink: #0d2a55;
    --backdrop: #d9d9d9;
  }
  * { margin: 0; padding: 0; box-sizing: border-box; }
  html, body { width: 1200px; height: 1200px; overflow: hidden; }
  body {
    background: var(--backdrop);
    font-family: "Montserrat", sans-serif;
    position: relative;
  }
  .flyer {
    position: absolute;
    left: 200px; top: 35px;
    width: 800px; height: 1130px;
    background: var(--white);
    overflow: hidden;
    box-shadow: 0 12px 40px rgba(0,0,0,.18);
  }
  .flyer-shapes { position: absolute; inset: 0; }
  .brand { position: absolute; left: 60px; top: 70px; color: var(--white); font-weight: 800; }
  .brand-mark { width: 90px; height: 90px; border-radius: 50%; background: var(--orange); margin-bottom: 18px; }
  .brand-name { font-size: 54px; line-height: 1; letter-spacing: 1px; }
  .brand-sub { font-size: 20px; letter-spacing: 4px; margin-top: 8px; }
  .offer-bubble {
    position: absolute; left: 40px; top: 330px;
    width: 300px; height: 180px;
    background: var(--orange); border-radius: 24px;
    color: var(--white); font-weight: 700; font-size: 27px; line-height: 1.2;
    padding: 26px 28px;
  }
  .offer-bubble::after {
    content: ""; position: absolute; left: 70px; bottom: -26px;
    border-left: 22px solid transparent; border-right: 22px solid transparent;
    border-top: 28px solid var(--orange);
  }
  .service-list { position: absolute; list-style: none; color: var(--blue); font-weight: 800; line-height: 1.2; }
  .service-list li { position: relative; padding-left: 34px; }
  .service-list li::before {
    content: ""; position: absolute; left: 0; top: 9px;
    width: 20px; height: 20px; border-radius: 50%;
    border: 4px solid var(--orange); background: var(--blue);
  }
  .services-main { left: 50px; top: 650px; font-size: 29px; width: 380px; }
  .services-extra { left: 440px; top: 700px; font-size: 27px; width: 340px; }
  .price-col { position: absolute; top: 868px; width: 200px; text-align: center; color: var(--white); }
  .price-title { font-weight: 800; font-size: 15px; letter-spacing: 1px; }
  .price-note { font-size: 12px; line-height: 1.3; margin-top: 4px; }
  .price-tag {
    position: absolute; top: 948px; width: 104px; height: 104px; border-radius: 50%;
    background: var(--white); color: var(--ink);
    font-weight: 800; font-size: 30px;
    display: flex; align-items: center; justify-content: center;
    box-shadow: 0 4px 12px rgba(0,0,0,.2);
  }
  .office { position: absolute; left: 60px; top: 1060px; color: var(--white); display: flex; gap: 14px; align-items: flex-start; }
  .office-label { font-size: 24px; font-weight: 500; }
  .office-address { font-size: 15px; font-weight: 700; letter-spacing: 1px; }
  .contact { position: absolute; right: 50px; top: 1066px; text-align: right; color: var(--white); }
  .social { display: flex; gap: 14px; justify-content: flex-end; margin-bottom: 8px; }
  .social span { width: 20px; height: 20px; border-radius: 50%; background: var(--orange); }
  .website { font-size: 17px; font-weight: 700; letter-spacing: 2px; }
</style>
</head>
<body>
<main class="flyer">
  <svg class="flyer-shapes" viewBox="0 0 800 1130" width="800" height="1130">
    <defs>
      <linearGradient id="photoTone" x1="0" y1="0" x2="1" y2="1">
        <stop offset="0" stop-color="#e9edf2"/>
        <stop offset=".55" stop-color="#4d74b5"/>
        <stop offset="1" stop-color="#1d3f7a"/>
      </linearGradient>
      <linearGradient id="roundTone" x1="0" y1="0" x2="1" y2="1">
        <stop offset="0" stop-color="#f2f2f2"/>
        <stop offset="1" stop-color="#3c63a8"/>
      </linearGradient>
    </defs>
    <path d="M0 0H800V420C600 470 300 470 0 400Z" fill="var(--blue)"/>
    <g role="img" aria-label="Photo of a plumber in blue overalls with a tool belt and pipe wrench">
      <path d="M390 0H800V445C700 490 610 520 520 540C450 380 410 200 390 0Z" fill="url(#photoTone)"/>
    </g>
    <path d="M390 0C410 200 450 380 520 540" fill="none" stroke="#fff" stroke-width="3" stroke-dasharray="2 8" stroke-linecap="round"/>
    <path class="swoosh" d="M330 602C500 585 680 525 800 440V505C680 575 500 622 330 626Z" fill="var(--orange)"/>
    <path class="swoosh-edge" d="M440 624C570 610 700 565 800 505V528C700 588 570 636 440 640Z" fill="var(--blue)"/>
    <circle cx="485" cy="585" r="92" fill="var(--orange)"/>
    <g role="img" aria-label="Photo of hands fitting a sink drain pipe">
      <circle cx="485" cy="585" r="78" fill="url(#roundTone)"/>
    </g>
    <circle cx="690" cy="540" r="92" fill="var(--orange)"/>
    <g role="img" aria-label="Photo of a smiling technician working under a kitchen sink">
      <circle cx="690" cy="540" r="78" fill="url(#roundTone)"/>
    </g>
    <path d="M0 1000C250 975 550 1005 800 1025V1130H0Z" fill="var(--blue)"/>
    <path d="M0 1012C250 988 550 1018 800 1038" fill="none" stroke="#fff" stroke-width="3" stroke-dasharray="2 8" stroke-linecap="round"/>
    <path d="M0 960C40 955 70 950 90 948V1000C60 1002 30 1005 0 1008Z" fill="var(--orange)"/>
    <rect x="90" y="850" width="660" height="165" rx="24" fill="var(--orange)"/>
    <path d="M750 960C770 962 790 965 800 966V1010L750 1010Z" fill="var(--orange)"/>
    <line x1="310" y1="875" x2="310" y2="990" stroke="#fff" stroke-width="2" stroke-dasharray="2 6"/>
    <line x1="530" y1="875" x2="530" y2="990" stroke="#fff" stroke-width="2" stroke-dasharray="2 6"/>
  </svg>

  <header class="brand">
    <div class="brand-mark"></div>
    <div class="brand-name">KEYSTONE</div>
    <div class="brand-sub">MECHANICAL INC</div>
  </header>

  <p class="offer-bubble">The discounted rates apply to the personal residence</p>

  <ul class="service-list services-main">
    <li>Boilers &amp; Controls</li>
    <li>Plumbing &amp; Heating</li>
    <li>HVAC &amp; Refrigeration</li>
  </ul>
  <ul class="service-list services-extra">
    <li>Preventative Maintenacne</li>
    <li>Gas fitting &amp; Drain Cleaning</li>
  </ul>

  <section class="price-col" style="left:100px">
    <div class="price-title">YOUR TITLE</div>
    <div class="price-note">Lorem ipsum dolor sit amet, consectetuer.</div>
  </section>
  <section class="price-col" style="left:320px">
    <div class="price-title">YOUR TITLE</div>
    <div class="price-note">Lorem ipsum dolor sit amet, consectetuer.</div>
  </section>
  <section class="price-col" style="left:540px">
    <div class="price-title">YOUR TITLE</div>
    <div class="price-note">Lorem ipsum dolor sit amet, consectetuer.</div>
  </section>
  <div class="price-tag" style="left:148px">$90</div>
  <div class="price-tag" style="left:368px">$90</div>
  <div class="price-tag" style="left:588px">$90</div>

  <footer>
    <div class="office">
      <svg width="26" height="34" viewBox="0 0 26 34" aria-hidden="true">
        <path d="M13 0C6 0 0 5.6 0 12.6 0 22 13 34 13 34S26 22 26 12.6C26 5.6 20 0 13 0Z" fill="#fff"/>
        <circle cx="13" cy="12.5" r="5" fill="var(--blue)"/>
      </svg>
      <div>
        <div class="office-label">Head Office</div>
        <div class="office-address">St. Lorem No. 7, NY City</div>
      </div>
    </div>
    <div class="contact">
      <div class="social"><span></span><span></span><span></span></div>
      <div class="website">WWW.KEYSTONEMECH.COM</div>
    </div>
  </footer>
</main>
</body>
</html>
```